Unique & Creative Business Card for Lumavessence

Would you please create a unique design that is soft and appealing to people who seek to raise vibrational energy for themselves, for animals (domestic or wild), or for the environment.

Optional: Elements could include, landscapes, wild animals, feathers, vibrational patterns, the elements (Earth, water, fire, air and space). Images that are calming.

With Thanks!

Target Market(s)

People and businesses who are into the environment, animal welfare, alternative health.

Contact Information for Business Card

Moira Bell
Energist
mb@lumavessence.example
lumavessence.example

Requirements
Must have
• Lumavessence logo (attached)
Symbols that represent our main services: Natural environment, animal, human and energy.
Our strapline ‘Achieving Vibrational Equilibrium’
Nice to have
• Clear and easy to read
Colours based on nature/soft colours

```html
<!DOCTYPE html>
<html lang="en">
<head>
<meta charset="utf-8">
<title>Lumavessence – Business Card</title>
<link rel="stylesheet" href="https://fonts.googleapis.com/css2?family=Arimo:wght@400;700&display=swap">
<style>
  :root {
    --page-bg: #eeeae6;
    --lavender: #e6dcec;
    --lavender-soft: #e9e1ef;
    --navy: #2b4a8e;
    --ring: #5b86c4;
    --teal: #1bb39c;
    --forest: #1d6a43;
    --forest-deep: #0f4a2c;
    --ink: #222;
    --white: #ffffff;
  }
  * { box-sizing: border-box; margin: 0; padding: 0; }
  html, body {
    width: 1200px; height: 900px; overflow: hidden;
    background: var(--page-bg);
    font-family: "Arimo", Arial, sans-serif;
  }
  .canvas { position: relative; width: 1200px; height: 900px; }

  .card {
    position: absolute; left: 270px; width: 660px; height: 377px;
    overflow: hidden;
    box-shadow: 0 6px 18px rgba(0,0,0,.18);
  }

  /* ---------- back of card ---------- */
  .card-back { top: 40px; background: var(--lavender); }
  .services {
    position: absolute; top: 52px; left: 0; right: 0;
    display: flex; justify-content: center; gap: 54px;
  }
  .service { width: 130px; text-align: center; }
  .service-badge {
    width: 104px; height: 104px; margin: 0 auto;
    border-radius: 50%;
    border: 3px solid var(--ring);
    padding: 6px;
    background: var(--white);
  }
  .service-badge-fill {
    width: 100%; height: 100%; border-radius: 50%;
    background: linear-gradient(180deg, var(--teal) 0%, var(--forest) 65%, var(--forest-deep) 100%);
  }
  .service-label {
    margin-top: 14px;
    color: var(--navy); font-weight: 700; font-size: 15px;
    letter-spacing: .04em; line-height: 1.1; text-transform: uppercase;
  }
  .forest-band {
    position: absolute; left: 0; right: 0; bottom: 0; height: 160px;
    background: linear-gradient(180deg, rgba(230,220,236,0) 0%, #b6b9c7 30%, #6f9c8a 60%, #2f7a56 100%);
  }

  /* ---------- front of card ---------- */
  .card-front { top: 478px; background: var(--white); }
  .card-front .wave { position: absolute; inset: 0; }
  .holder { position: absolute; left: 54px; top: 62px; }
  .holder-name {
    color: var(--navy); font-weight: 700; font-size: 30px; letter-spacing: .02em;
    text-transform: uppercase;
  }
  .holder-role { color: var(--ink); font-size: 19px; margin-top: 2px; }

  .contact-list {
    position: absolute; left: 76px; top: 198px; list-style: none;
    color: var(--ink); font-size: 17px; line-height: 1.45;
  }
  .contact-list li { display: flex; align-items: center; gap: 10px; }
  .contact-list svg { width: 18px; height: 18px; flex: none; }

  .brand {
    position: absolute; right: 46px; top: 66px;
    display: flex; align-items: center; gap: 10px;
  }
  .brand-mark {
    width: 26px; height: 26px; border-radius: 50%;
    border: 3px solid var(--ring);
  }
  .brand-name {
    color: var(--navy); font-size: 26px; font-weight: 400;
    letter-spacing: .03em; text-transform: uppercase;
  }

  .strapline {
    position: absolute; left: 236px; bottom: 30px;
    color: var(--white); font-size: 17px; letter-spacing: .03em;
    text-transform: uppercase; white-space: nowrap;
    transform: rotate(-9deg); transform-origin: left bottom;
  }
</style>
</head>
<body>
<main class="canvas">

  <section class="card card-back" aria-label="Card back: services">
    <div class="services">
      <div class="service">
        <div class="service-badge"><div class="service-badge-fill" role="img" aria-label="Natural environment symbol: globe with leaf"></div></div>
        <p class="service-label">Natural<br>Environment</p>
      </div>
      <div class="service">
        <div class="service-badge"><div class="service-badge-fill" role="img" aria-label="Animal symbol: bear silhouette"></div></div>
        <p class="service-label">Animal</p>
      </div>
      <div class="service">
        <div class="service-badge"><div class="service-badge-fill" role="img" aria-label="Human and energy symbol: sun with lightning bolt"></div></div>
        <p class="service-label">Human and<br>Energy</p>
      </div>
    </div>
    <div class="forest-band" role="img" aria-label="Misty watercolour pine forest with flying birds"></div>
  </section>

  <section class="card card-front" aria-label="Card front: contact">
    <svg class="wave" viewBox="0 0 660 377" preserveAspectRatio="none" aria-hidden="true">
      <path d="M0 318 C 180 300, 330 290, 470 210 C 560 160, 620 130, 660 122 L660 377 L0 377 Z" fill="var(--lavender-soft)"/>
      <path d="M0 340 C 200 330, 340 310, 480 230 C 560 185, 620 160, 660 150 L660 377 L0 377 Z" fill="var(--navy)"/>
    </svg>

    <div class="holder">
      <h1 class="holder-name">Moira Bell</h1>
      <p class="holder-role">Energist</p>
    </div>

    <div class="brand">
      <span class="brand-mark"></span>
      <span class="brand-name">Lumavessence</span>
    </div>

    <ul class="contact-list">
      <li>
        <svg viewBox="0 0 24 24"><path fill="var(--navy)" d="M6.6 10.8a15 15 0 0 0 6.6 6.6l2.2-2.2a1 1 0 0 1 1-.25 11.4 11.4 0 0 0 3.6.57 1 1 0 0 1 1 1V20a1 1 0 0 1-1 1A17 17 0 0 1 3 4a1 1 0 0 1 1-1h3.5a1 1 0 0 1 1 1c0 1.25.2 2.45.57 3.57a1 1 0 0 1-.25 1z"/></svg>
        5550192746
      </li>
      <li>
        <svg viewBox="0 0 24 24"><rect x="2" y="5" width="20" height="14" fill="var(--navy)"/><path d="M2 5l10 8 10-8" fill="none" stroke="#fff" stroke-width="1.6"/></svg>
        mb@lumavessence.example
      </li>
      <li>
        <svg viewBox="0 0 24 24" fill="none" stroke="var(--navy)" stroke-width="1.8"><circle cx="12" cy="12" r="9"/><ellipse cx="12" cy="12" rx="4" ry="9"/><path d="M3 12h18M5 7h14M5 17h14"/></svg>
        www.lumavessence.example
      </li>
    </ul>

    <p class="strapline">Achieving Vibrational Equilibrium</p>
  </section>

</main>
</body>
</html>
```